Company E-mail Signature

Hello!

I know what I want to do for our company's updated e-mail signature (Please see attached "Autumn 2023 email sig edit"). However, my skills are exceptionally limited and I am unable to work out, or find information on converting this into an e-mail signature, with clickable social media links.
This is for Microsoft Outlook and would need to be edited for 11 members of staff.
All help or any slight improvement suggestions are most welcome!

```html
<!DOCTYPE html>
<html lang="en">
<head>
<meta charset="utf-8">
<title>Eastfield – E-mail Signature</title>
<link rel="stylesheet" href="https://fonts.googleapis.com/css2?family=Josefin+Sans:wght@400;600&family=Carlito:ital,wght@0,400;1,400&display=swap">
<style>
  :root {
    --band-brown: #3c230f;
    --gold: #d8b56c;
    --white: #ffffff;
    --purple: #7a3aa8;
    --green: #8fc463;
    --page: #ffffff;
  }
  html, body {
    margin: 0;
    padding: 0;
    overflow: hidden;
    background: var(--page);
  }
  .signature {
    position: relative;
    width: 1200px;
    height: 801px;
    overflow: hidden;
    background: var(--page);
    font-family: "Carlito", Calibri, sans-serif;
  }
  .header-band {
    position: absolute;
    left: 0; top: 0;
    width: 1200px; height: 205px;
    background: var(--band-brown);
  }
  .brand {
    position: absolute;
    left: 34px; top: 92px;
    font-family: "Josefin Sans", sans-serif;
    font-weight: 600;
    font-size: 58px;
    line-height: 1;
    color: var(--gold);
    letter-spacing: 1px;
  }
  .person-name {
    position: absolute;
    left: 386px; top: 16px;
    margin: 0;
    font-family: "Josefin Sans", sans-serif;
    font-weight: 400;
    font-size: 37px;
    color: var(--gold);
  }
  .person-role {
    position: absolute;
    left: 386px; top: 78px;
    margin: 0;
    font-family: "Josefin Sans", sans-serif;
    font-weight: 400;
    font-size: 33px;
    color: var(--white);
  }
  .contact-row {
    position: absolute;
    left: 386px; top: 130px;
    display: flex;
    align-items: center;
    font-family: "Josefin Sans", sans-serif;
    font-size: 23px;
    color: var(--white);
  }
  .contact-item { display: flex; align-items: center; }
  .contact-item svg { margin-right: 12px; }
  .contact-item + .contact-item { margin-left: 26px; }
  .social-links {
    position: absolute;
    left: 1131px; top: 5px;
    display: flex;
    flex-direction: column;
    gap: 12px;
  }
  .social-link {
    display: block;
    width: 57px; height: 57px;
    border-radius: 12px;
    background: var(--gold);
  }
  .fleet-photo {
    position: absolute;
    left: 0; top: 205px;
    width: 1200px; height: 412px;
    background: linear-gradient(180deg,
      #d9d6d2 0%, #c9a889 18%, #b8703a 38%, #7a4a2a 55%,
      #5b3a25 68%, #8a8480 82%, #9c9894 100%);
  }
  .notes {
    position: absolute;
    left: 0; top: 620px;
    width: 1200px;
    font-style: italic;
    font-size: 19.5px;
    line-height: 1.4;
  }
  .notes p { margin: 0; position: absolute; white-space: nowrap; }
  .notes-heading { left: 13px; top: 7px; color: var(--purple); text-decoration: underline; }
  .notes-validity { left: 13px; top: 45px; color: var(--purple); }
  .notes-carbon { left: 24px; top: 72px; color: var(--green); white-space: normal !important; width: 1160px; text-indent: 54px; }
  .notes-print { left: 12px; top: 136px; display: flex; align-items: center; color: var(--green); }
  .notes-print svg { margin-right: 14px; }
</style>
</head>
<body>
<div class="signature">
  <header class="header-band">
    <div class="brand">Eastfield</div>
    <h1 class="person-name">Sam Hartley</h1>
    <h2 class="person-role">Manager</h2>
    <div class="contact-row">
      <span class="contact-item">
        <svg width="30" height="30" viewBox="0 0 24 24" aria-hidden="true">
          <path d="M6.6 10.8a15.2 15.2 0 0 0 6.6 6.6l2.2-2.2a1 1 0 0 1 1-.25 11.4 11.4 0 0 0 3.6.57 1 1 0 0 1 1 1V20a1 1 0 0 1-1 1A17 17 0 0 1 3 4a1 1 0 0 1 1-1h3.5a1 1 0 0 1 1 1c0 1.25.2 2.45.57 3.6a1 1 0 0 1-.25 1z" fill="var(--gold)"/>
          <path d="M15 3a6 6 0 0 1 6 6M15 6.5A2.5 2.5 0 0 1 17.5 9" stroke="var(--gold)" stroke-width="1.6" fill="none" stroke-linecap="round"/>
        </svg>
        0201 555 0184
      </span>
      <span class="contact-item">
        <svg width="38" height="28" viewBox="0 0 38 28" aria-hidden="true">
          <rect x="1.5" y="1.5" width="35" height="25" fill="none" stroke="var(--gold)" stroke-width="2"/>
          <path d="M1.5 1.5 19 16 36.5 1.5M1.5 26.5 14 12M36.5 26.5 24 12" fill="none" stroke="var(--gold)" stroke-width="2"/>
        </svg>
        sam.hartley@eastfield-coaches.co.uk
      </span>
    </div>
    <nav class="social-links" aria-label="Social media">
      <a class="social-link" href="#" aria-label="Photo sharing profile"></a>
      <a class="social-link" href="#" aria-label="Social network page"></a>
      <a class="social-link" href="#" aria-label="Professional network profile"></a>
    </nav>
  </header>

  <div class="fleet-photo" role="img" aria-label="Photograph of two brown coaches parked nose to nose in a car park, with autumn trees behind them"></div>

  <section class="notes">
    <p class="notes-heading">IMPORTANT</p>
    <p class="notes-validity">Please note all quotations are valid for five days only.</p>
    <p class="notes-carbon">As part of our drive to become a Carbon Neutral company, for every booking made, Eastfield will plant a tree on your behalf to offset our footprint.</p>
    <p class="notes-print">
      <svg width="40" height="38" viewBox="0 0 40 38" aria-hidden="true">
        <path d="M20 18V8M20 10c-4-6-10-4-10-4s1 6 10 4zM20 10c4-6 10-4 10-4s-1 6-10 4z" fill="none" stroke="var(--green)" stroke-width="1.6" stroke-linejoin="round"/>
        <path d="M2 28h8l6 4h10c2 0 2-3 0-3h-8M18 29l12-5c2-1 4 1 2 3l-12 8H2" fill="none" stroke="var(--green)" stroke-width="1.6" stroke-linejoin="round" stroke-linecap="round"/>
      </svg>
      Please consider the Environment before printing this e-mail. Thank you
    </p>
  </section>
</div>
</body>
</html>
```